Client website

Our designer we were working with had some personal things come up and was unable to finish the design for the site.

We have a .psd file started, and will be attaching it to the project.
Updates

Reason: I still want to polish the designs with the current designer and allow more designers the opportunity to participate.

Reason: I'm extending the deadline for another day to give everyone enough time for the final changes our client wants.

I'm trying to extend the deadline so we can get one last set of comps in for my client.  Could everyone message me and let me know how much time they need to do the final tweaks?

Reason: Hey everyone.  I've been sick the last 3 days and I haven't been able to provide feedback on designs.  I'm extending just a few more days so I can catch up here.  Thanks everyone for your patience.

Target Market(s)

Adults in United States aged 25 to 60 that handle the household budgets and maintenance.

Requirements
Must have
• 1) We need 2 pages. 1 page for flood restoration, 1 page for carpet cleaning

2) The 1-800-# must be the focal point of the website for both pages. People are mostly looking to contact someone ASAP to get them out to their house when flooding occurs.

3) We''re going to have a slide show area to high-light different sub-services offered for each page.

4) We really want a frendloop / quipsy feed area. We''re going to use frendloop for special offers, and quipsy for weather updates. The frendloop feed is going to be on the carpet cleaning page. The quipsy feed is going to be on the flood page.

5) We want an SEO text sections near the bottom.

6) The very bottom will link to the privacy policy and user agreement as well as company name and copyright details.

We really want to stick to the say "theme" that our first designer started with.
Nice to have
• I'm not a designer, so if you think something looks better somewhere, or something can be eliminated, or something can be enhanced, but all means, let us know.

```html
<!DOCTYPE html>
<html lang="en">
<head>
<meta charset="utf-8">
<title>Aqua-Vera — Water &amp; Fire Damage Restoration</title>
<link rel="stylesheet" href="https://fonts.googleapis.com/css2?family=Source+Sans+3:wght@400;600;700&family=Arimo:wght@400&family=Gloria+Hallelujah&display=swap">
<style>
  :root {
    --page-dark: #1c2733;
    --column-top: #bfe1f6;
    --column-mid: #4f93cf;
    --column-deep: #1f5a93;
    --column-floor: #12365e;
    --edge-blue: #1b6fd0;
    --nav-blue: #3aa2e6;
    --nav-blue-dark: #1f7fcf;
    --nav-green: #2fb83a;
    --panel-fill: rgba(196, 222, 240, 0.78);
    --panel-feed: rgba(176, 200, 222, 0.82);
    --heading-blue: #1e77c0;
    --body-grey: #5b6670;
    --body-dark: #1a1f26;
    --button-green: #23a827;
    --button-green-light: #4fd34b;
    --seo-text: #55779c;
    --footer-text: #ffffff;
    --note-paper: #f1eee4;
    --brand-green: #1aa34a;
  }
  * { box-sizing: border-box; margin: 0; padding: 0; }
  html, body { width: 1200px; height: 1200px; overflow: hidden; }
  body {
    background: radial-gradient(ellipse at center, #2a3947 0%, var(--page-dark) 70%);
    font-family: "Arimo", Arial, sans-serif;
    position: relative;
  }
  .site-column {
    position: absolute; left: 135px; top: 0; width: 933px; height: 1200px;
    background: linear-gradient(180deg, var(--column-top) 0%, #d7eefb 22%, #8cc4ea 32%, var(--column-mid) 52%, var(--column-deep) 72%, var(--column-floor) 100%);
    border-left: 3px solid var(--edge-blue);
    border-right: 3px solid var(--edge-blue);
    box-shadow: 0 0 40px rgba(0,0,0,0.6);
  }
  .header-scene {
    position: absolute; left: 138px; top: 0; width: 927px; height: 312px;
    background:
      radial-gradient(ellipse 260px 60px at 340px 150px, rgba(120,185,230,0.55), transparent 70%),
      linear-gradient(170deg, transparent 35%, rgba(95,160,215,0.45) 42%, rgba(180,220,245,0.3) 55%, transparent 62%),
      linear-gradient(180deg, #3d8fe0 0%, #88c3ef 35%, #d9f0fc 75%, #e8f6fd 100%);
  }
  .brand { position: absolute; left: 187px; top: 205px; display: flex; align-items: center; gap: 10px; }
  .brand-mark { width: 26px; height: 26px; border-radius: 50%; background: var(--brand-green); }
  .brand-name {
    font-family: "Source Sans 3", sans-serif; font-weight: 700;
    font-size: 40px; color: var(--brand-green); letter-spacing: 1px; line-height: 1;
  }
  .brand-tagline {
    position: absolute; left: 197px; top: 250px;
    font-family: "Source Sans 3", sans-serif; font-size: 15px; font-weight: 600;
    color: #1f73c4; font-variant: small-caps; letter-spacing: 0.5px;
  }
  .main-nav {
    position: absolute; left: 140px; top: 315px; width: 925px; height: 36px;
    display: flex; background: linear-gradient(180deg, #6cc0f2, var(--nav-blue-dark));
  }
  .main-nav a {
    width: 147px; height: 36px; text-align: center; line-height: 36px;
    color: #fff; text-decoration: none; font-family: "Source Sans 3", sans-serif;
    font-size: 17px; letter-spacing: 1px;
    background: linear-gradient(180deg, #5fb8f0, var(--nav-blue-dark));
    border-right: 1px solid rgba(255,255,255,0.6);
  }
  .main-nav a.is-current { background: linear-gradient(180deg, #4fd34b, var(--nav-green)); }
  .call-note {
    position: absolute; left: 900px; top: 185px; width: 230px; height: 190px;
    background: var(--note-paper); transform: rotate(22deg);
    box-shadow: 3px 5px 10px rgba(0,0,0,0.35), 6px 10px 0 -2px #e3dfd2;
    padding: 32px 14px 0 22px; font-family: "Gloria Hallelujah", cursive; color: #2a2a2a;
  }
  .call-note .note-title { font-size: 30px; line-height: 1.2; }
  .call-note .note-phone { font-size: 21px; margin-top: 6px; }
  .note-pin { position: absolute; left: 948px; top: 155px; width: 22px; height: 22px; border-radius: 50%; background: #2bb52d; box-shadow: 1px 2px 3px rgba(0,0,0,0.4); }
  .slide-panel {
    position: absolute; left: 178px; top: 395px; width: 844px; height: 297px;
    background: var(--panel-fill); border-radius: 14px; box-shadow: 0 3px 8px rgba(0,40,90,0.35);
  }
  .slide-title {
    position: absolute; left: 44px; top: 38px;
    font-family: "Source Sans 3", sans-serif; font-weight: 700; font-size: 50px;
    letter-spacing: -2px; color: var(--heading-blue); text-shadow: 0 1px 0 #fff;
  }
  .slide-copy { position: absolute; left: 48px; top: 130px; width: 510px; font-size: 16px; line-height: 18px; color: var(--body-grey); }
  .slide-copy p + p { margin-top: 18px; }
  .action-button {
    position: absolute; left: 614px; top: 171px; width: 176px; height: 44px;
    border-radius: 8px; background: linear-gradient(180deg, var(--button-green-light), var(--button-green));
    color: #fff; font-family: "Source Sans 3", sans-serif; font-weight: 700; font-size: 23px;
    text-align: center; line-height: 44px; text-decoration: none; letter-spacing: -0.5px;
    box-shadow: 0 2px 4px rgba(0,0,0,0.3);
  }
  .slide-arrow { position: absolute; top: 522px; width: 45px; height: 45px; }
  .slide-arrow.prev { left: 155px; }
  .slide-arrow.next { left: 999px; }
  .feed-box {
    position: absolute; width: 400px; height: 172px;
    background: var(--panel-feed); border-radius: 8px; box-shadow: 0 3px 8px rgba(0,30,70,0.35);
  }
  .feed-box.frendloop { left: 178px; top: 733px; }
  .feed-box.quipsy { left: 621px; top: 736px; }
  .feed-badge { position: absolute; left: 36px; top: 40px; width: 80px; text-align: center; }
  .feed-badge .badge-square { width: 62px; height: 62px; margin: 0 auto; border-radius: 8px; background: #e8eef5; display: flex; align-items: center; justify-content: center; font-family: "Source Sans 3", sans-serif; font-weight: 600; font-size: 13px; color: #2d5c99; }
  .feed-badge .follow { margin-top: 8px; background: #fff; font-size: 11px; color: #111; height: 20px; line-height: 20px; box-shadow: 0 1px 2px rgba(0,0,0,0.35); }
  .feed-title { position: absolute; left: 142px; top: 28px; font-family: "Source Sans 3", sans-serif; font-weight: 700; font-size: 31px; letter-spacing: -1px; color: var(--heading-blue); }
  .feed-text { position: absolute; left: 142px; top: 70px; width: 245px; font-size: 13px; line-height: 15px; color: var(--body-dark); }
  .seo-text { position: absolute; left: 179px; top: 957px; width: 845px; font-size: 10.5px; line-height: 15px; color: var(--seo-text); }
  .site-footer { position: absolute; left: 179px; top: 1078px; width: 846px; display: flex; justify-content: space-between; font-size: 11px; color: var(--footer-text); }
  .site-footer a { color: var(--footer-text); text-decoration: none; }
  .diver-art { position: absolute; left: 882px; top: 1100px; width: 128px; height: 66px; border-radius: 30px; background: radial-gradient(ellipse, rgba(60,170,150,0.7), rgba(20,70,90,0) 75%); }
</style>
</head>
<body>
  <div class="site-column"></div>
  <div class="header-scene" role="img" aria-label="Bright sky with clouds and a splashing wave of clear water"></div>

  <div class="brand">
    <span class="brand-mark"></span>
    <span class="brand-name">AQUA-VERA</span>
  </div>
  <div class="brand-tagline">Water &amp; Fire Damage Restoration</div>

  <nav class="main-nav">
    <a href="#" class="is-current">home</a>
    <a href="#">about</a>
    <a href="#">services</a>
    <a href="#">faq</a>
    <a href="#">contact</a>
  </nav>

  <div class="call-note">
    <div class="note-title">Call Us Now!</div>
    <div class="note-phone">1-800-555-0142</div>
  </div>
  <div class="note-pin"></div>

  <section class="slide-panel">
    <h1 class="slide-title">Sub-service Number One</h1>
    <div class="slide-copy">
      <p>Lorem ipsum dolor sit amet, consectetur adipiscing elit. Duis semper, turpis in sodales ultricies, felis dui facilisis sem, nec dignissim augue nisl eu eros. Sed a faucibus massa.</p>
      <p>Suspendisse id felis tellus, vel sagittis sem. Fusce aliquam scelerisque diam et tempor.</p>
    </div>
    <a href="#" class="action-button">A Button »</a>
  </section>

  <svg class="slide-arrow prev" viewBox="0 0 45 45" aria-label="Previous slide">
    <circle cx="22.5" cy="22.5" r="21" fill="#1f8fe0" stroke="#fff" stroke-width="2"/>
    <path d="M24 14 L16 22.5 L24 31 M31 14 L23 22.5 L31 31" fill="none" stroke="#fff" stroke-width="3.5" stroke-linecap="round"/>
  </svg>
  <svg class="slide-arrow next" viewBox="0 0 45 45" aria-label="Next slide">
    <circle cx="22.5" cy="22.5" r="21" fill="#1f8fe0" stroke="#fff" stroke-width="2"/>
    <path d="M14 14 L22 22.5 L14 31 M21 14 L29 22.5 L21 31" fill="none" stroke="#fff" stroke-width="3.5" stroke-linecap="round"/>
  </svg>

  <section class="feed-box frendloop">
    <div class="feed-badge"><div class="badge-square">frendloop</div><div class="follow">Follow us!</div></div>
    <h2 class="feed-title">frendloop Feed</h2>
    <p class="feed-text">- Lorem ipsum dolor sit amet, consectetur adipiscing elit. Duis semper, turpis in sodales ultricies, felis dui facilisis sem, nec dignissim</p>
  </section>

  <section class="feed-box quipsy">
    <div class="feed-badge"><div class="badge-square">quipsy</div><div class="follow">Follow us!</div></div>
    <h2 class="feed-title">quipsy Feed</h2>
    <p class="feed-text">- Lorem ipsum dolor sit amet, consectetur adipiscing elit. Duis semper, turpis in sodales ultricies, felis dui facilisis sem, nec dignissim</p>
  </section>

  <p class="seo-text">Lorem ipsum dolor sit amet, consectetur adipiscing elit. Etiam mattis dolor placerat sem iaculis dapibus. Praesent velit nibh, sollicitudin vel feugiat sit amet, bibendum id urna. Etiam eleifend tellus a turpis rutrum mollis et non massa. Vivamus eu porta felis. Etiam sodales enim magna, eu imperdiet nulla. Duis tincidunt enim ut massa faucibus ullamcorper. Donec ac sem odio, ut convallis risus. Suspendisse gravida vestibulum bibendum. Aenean aliquet dui quis justo sollicitudin sit amet euismod libero facilisis. Donec consectetur elit luctus lacus consequat ut porttitor risus varius. Pellentesque interdum, sem sed commodo ornare, sem est semper turpis, a viverra sem enim a erat. Cras sollicitudin leo id magna condimentum faucibus. Class aptent taciti sociosqu ad litora torquent per conubia nostra, per inceptos himenaeos. In vulputate eros non sodales placerat, dolor lectus sollicitudin augue, elementum semper elit leo vel nulla. Aenean faucibus cursus magna in ornare. Nunc porta, purus porta egestas ornare, nunc nisl molestie sem, id aliquam nisi justo quis massa. In id placerat nibh. Aliquam risus mi, rhoncus et lacinia ac, pharetra convallis ipsum. Phasellus volutpat turpis vitae</p>

  <footer class="site-footer">
    <span>Copyright 2010. Aqua-Vera.</span>
    <span><a href="#">Privacy Policy</a> | <a href="#">User Agreement</a></span>
  </footer>

  <div class="diver-art" role="img" aria-label="Small scuba diver swimming with a glowing torch"></div>
</body>
</html>
```